New Business Card Design Project

I have a logo I would like to use on the business card. I want something that will stand out and that will be remembered.

Target Market(s)

People who collect gems, minerals and crystals.

Contact Information for Business Card

email - mkthestonefalcon@vendrollo.com
phone # 917-406-2581

Font styles to use
Serif
Sans Serif
Decorative

Colors

Designer to choose colors to be used in the design.

Requirements
Must have
• The logo...two to choose from.
Nice to have
• An eye catching and memorable way to draw in people who collect gems minerals and crystals.

```html
<!DOCTYPE html>
<html lang="en">
<head>
<meta charset="utf-8">
<title>The Stone Falcon – Business Card</title>
<link href="https://fonts.googleapis.com/css2?family=Libre+Baskerville:wght@400;700&display=swap" rel="stylesheet">
<style>
  :root {
    --backdrop: #e6e8ec;
    --card-paper: #fbfbfa;
    --card-edge: #e3e3e1;
    --ink: #1a1a1a;
    --accent-blue: #2f45a8;
    --wash-light: #cfe6f4;
    --wash-mid: #7ec0e6;
    --wash-deep: #3f9bd3;
  }
  * { box-sizing: border-box; margin: 0; padding: 0; }
  html, body {
    width: 1200px;
    height: 1005px;
    overflow: hidden;
    background: var(--backdrop);
  }
  .canvas {
    position: relative;
    width: 1200px;
    height: 1005px;
  }
  .business-card {
    position: absolute;
    left: 340px;
    top: 47px;
    width: 520px;
    height: 910px;
    background: var(--card-paper);
    border: 1px solid var(--card-edge);
    box-shadow: 0 6px 24px rgba(0,0,0,0.12);
    overflow: hidden;
    font-family: "Libre Baskerville", Georgia, serif;
    color: var(--ink);
  }
  .brand {
    position: absolute;
    left: 0;
    right: 0;
    top: 120px;
    display: flex;
    flex-direction: column;
    align-items: center;
  }
  .brand-mark {
    width: 230px;
    height: 230px;
    border-radius: 50%;
    background: var(--ink);
    margin-bottom: 34px;
  }
  .brand-name {
    font-size: 46px;
    font-weight: 700;
    line-height: 1.1;
    color: var(--ink);
    text-align: center;
    white-space: nowrap;
  }
  .brand-tagline {
    margin-top: 18px;
    padding-top: 14px;
    border-top: 3px solid var(--accent-blue);
    font-size: 17px;
    font-weight: 400;
    letter-spacing: 3px;
    text-transform: uppercase;
    color: var(--accent-blue);
    white-space: nowrap;
  }
  .contact {
    position: absolute;
    left: 0;
    right: 0;
    top: 585px;
    text-align: center;
    z-index: 2;
  }
  .contact-phone {
    font-size: 36px;
    letter-spacing: 1px;
    margin-bottom: 26px;
  }
  .contact-email {
    font-size: 22px;
    white-space: nowrap;
  }
  .watercolor-band {
    position: absolute;
    left: 0;
    right: 0;
    bottom: 0;
    height: 300px;
    background: linear-gradient(180deg,
      rgba(207,230,244,0) 0%,
      var(--wash-light) 20%,
      var(--wash-mid) 58%,
      var(--wash-deep) 100%);
    z-index: 1;
  }
</style>
</head>
<body>
<main class="canvas">
  <section class="business-card">
    <div class="brand">
      <span class="brand-mark"></span>
      <span class="brand-name">The Stone Falcon</span>
      <span class="brand-tagline">Gems · Minerals · Crystals</span>
    </div>
    <div class="watercolor-band" role="img" aria-label="Blue watercolor wash along the bottom edge of the card"></div>
    <div class="contact">
      <p class="contact-phone">917-406-2581</p>
      <p class="contact-email">mkthestonefalcon@vendrollo.com</p>
    </div>
  </section>
</main>
</body>
</html>
```